BRIGHT HEARTH - A5 flyer design

Please see updated brief attached

We need an engaging A5 flyer to accompany a targeted mail out to help recruit households to our BRIGHT HEARTH project

Warmwell Aid is a small environmental small charity based in NW London. We work to improve the health and well being of vulnerable people and communities living in fuel poverty. Through educating, advising and supporting, we provide practical solutions that enable people to live in warm, dry and comfortable homes, in control of their fuel use and their fuel costs.

We have recently been awarded a grant to run a project to conduct in home trials to test two new and innovative energy saving measures. The project is called BRIGHT HEARTH.

Aim of Flyer: to immediately engage households in want to partake in the project. It will be accompanied with a letter giving more in depth details about the project, criteria for participating etc so the flyer will not need to carry all the detail

Target Audience: Households in fuel poverty predominately from the social housing sector, low income, ethnically diverse and may have vulnerable household members (e.g. long term health conditions, debts, elderly etc)

More details in full brief attached.
Contact: dan@warmwellaid.org.uk or 020 7946 0718

Target Market(s)

low income households in fuel poverty - NW London area

Requirements
Must have
• Project name
• Company logo/s
Nice to have
• highlight how the project can save people money/energy
• Free to participate in project
• highlight the chance to win prizes for partaking

```html
<!DOCTYPE html>
<html lang="en">
<head>
<meta charset="utf-8">
<title>Bright Hearth – A5 Flyer</title>
<link rel="stylesheet" href="https://fonts.googleapis.com/css2?family=Montserrat:wght@700;800;900&display=swap">
<style>
  :root {
    --sky-top: #6f7fd6;
    --sky-mid: #3a3f9e;
    --night: #0d0f3a;
    --glow: #ffffff;
    --glow-blue: #a9c8ff;
    --crowd-dark: #0a0b22;
    --crowd-light: #4a5a9a;
    --gold: #f4b400;
    --gold-dark: #b27600;
    --gold-light: #ffe27a;
    --badge-ring: #1b1b1b;
    --white: #ffffff;
  }
  * { margin: 0; padding: 0; box-sizing: border-box; }
  html, body { width: 847px; height: 1200px; overflow: hidden; background: var(--night); }
  .flyer {
    position: relative;
    width: 847px; height: 1200px; overflow: hidden;
    font-family: "Montserrat", Arial, sans-serif;
    color: var(--white);
    background: linear-gradient(180deg, var(--sky-top) 0%, var(--sky-mid) 45%, var(--night) 100%);
  }
  .project-title {
    position: absolute; top: 40px; left: 0; width: 100%;
    text-align: center; font-weight: 800; font-size: 86px; letter-spacing: 1px;
    line-height: 1;
  }
  .light-hands {
    position: absolute; left: 120px; top: 240px; width: 610px; height: 560px;
    background: radial-gradient(circle at 50% 50%, var(--glow) 0%, var(--glow) 14%, var(--glow-blue) 30%, rgba(100,130,230,0.35) 55%, rgba(60,70,170,0) 72%);
  }
  .crowd {
    position: absolute; left: 0; top: 810px; width: 100%; height: 390px;
    background: linear-gradient(180deg, var(--crowd-light) 0%, #1d2460 35%, var(--crowd-dark) 100%);
  }
  .prize-badge { position: absolute; left: 24px; top: 790px; width: 176px; height: 176px; }
  .savings-copy {
    position: absolute; left: 44px; top: 995px; width: 260px;
    font-weight: 800; font-size: 20px; line-height: 1.22;
  }
  .savings-figure {
    position: absolute; left: 304px; top: 998px;
    font-weight: 900; line-height: 0.95;
  }
  .savings-figure .percent { display: block; font-size: 74px; }
  .savings-figure .up-to { display: block; font-size: 70px; }
  .free-offer {
    position: absolute; left: 562px; top: 895px; width: 270px; font-weight: 800;
  }
  .free-offer .free { display: block; font-size: 104px; line-height: 1; }
  .free-offer .detail { display: block; font-size: 34px; line-height: 1.1; }
  .org-name {
    position: absolute; left: 566px; top: 1120px;
    font-weight: 700; font-size: 30px; color: var(--white);
  }
</style>
</head>
<body>
<main class="flyer">
  <div class="light-hands" role="img" aria-label="Cupped hands holding a bright glowing ball of light"></div>
  <div class="crowd" role="img" aria-label="Large crowd of people gathered in silhouette below the light"></div>

  <h1 class="project-title">BRIGHT HEARTH</h1>

  <svg class="prize-badge" viewBox="0 0 186 186" aria-label="Chance to win prizes for partaking">
    <defs>
      <radialGradient id="goldFill" cx="45%" cy="40%" r="60%">
        <stop offset="0%" stop-color="var(--gold-light)"/>
        <stop offset="60%" stop-color="var(--gold)"/>
        <stop offset="100%" stop-color="var(--gold-dark)"/>
      </radialGradient>
      <path id="ringTop" d="M 30 93 A 63 63 0 0 1 156 93"/>
      <path id="ringBottom" d="M 24 93 A 69 69 0 0 0 162 93"/>
    </defs>
    <circle cx="93" cy="93" r="90" fill="url(#goldFill)"/>
    <circle cx="93" cy="93" r="80" fill="var(--badge-ring)"/>
    <circle cx="93" cy="93" r="48" fill="url(#goldFill)"/>
    <text font-family="Montserrat, Arial, sans-serif" font-weight="800" font-size="17" fill="var(--gold)">
      <textPath href="#ringTop" startOffset="50%" text-anchor="middle">Chance to Win</textPath>
    </text>
    <text font-family="Montserrat, Arial, sans-serif" font-weight="800" font-size="17" fill="var(--gold)">
      <textPath href="#ringBottom" startOffset="50%" text-anchor="middle">for Partaking</textPath>
    </text>
    <text x="93" y="101" text-anchor="middle" font-family="Montserrat, Arial, sans-serif" font-weight="800" font-size="24" fill="var(--badge-ring)">Prizes</text>
  </svg>

  <p class="savings-copy">New Energy Saving<br>Measures that we<br>will be Trailing will<br>Potentially Reduce<br>Energy Costs by</p>
  <p class="savings-figure"><span class="percent">40%</span><span class="up-to">up to</span></p>

  <p class="free-offer"><span class="free">Free</span><span class="detail">Participation<br>In Project</span></p>

  <p class="org-name">Warmwell Aid</p>
</main>
</body>
</html>
```